Postcard Design

We are a licensed and insured remodeling contractor in Johnson County, KS. I am looking to get a professional look for our postcard advertising. I would prefer something that appeals to women, but is still masculine enough for a contractor. Here is the verbiage I would like in the postcard.
Ever question the references you get from a contractor? Wouldn't you prefer to get a reference from your neighbor?
We are currently working with one of your neighbors and would love the opportunity to work for you. You can look us up on our website and see some of the wonderful spaces we have helped create. Call us today to schedule an appointment and let us know how we can help you create the new space you have always dreamed of.
Tel: 913-552-0187
Fax:913-530-2814
WWW.BELTRANEHOMEWORKS.EXAMPLE
BELTRANEHOMEWORKS@MAILBOX.EXAMPLE
Here is the verbiage I would like to use.
We are working in your neighborhood.
Tel: 913-552-0187
Fax:913-530-2814
Contractor

```html
<!DOCTYPE html>
<html lang="en">
<head>
<meta charset="utf-8">
<title>Beltrane Home Works – Neighbor Postcard</title>
<link rel="stylesheet" href="https://fonts.googleapis.com/css2?family=Exo+2:ital,wght@0,600;0,700;1,500;1,600&display=swap">
<style>
  :root {
    --navy-deep: #0f1f2c;
    --navy: #1d3447;
    --navy-text: #13263a;
    --steel: #5d7f99;
    --orange: #f5921e;
    --orange-light: #f9a632;
    --white: #ffffff;
    --wood-dark: #5a3318;
    --wood: #a1602c;
    --stone: #c9b79a;
  }
  html, body {
    margin: 0;
    padding: 0;
    width: 1200px;
    height: 926px;
    overflow: hidden;
    background: var(--navy-deep);
  }
  .postcard {
    position: relative;
    width: 1200px;
    height: 926px;
    overflow: hidden;
    font-family: "Exo 2", sans-serif;
    color: var(--white);
  }
  .postcard__shapes {
    position: absolute;
    inset: 0;
  }
  .intro {
    position: absolute;
    top: 50px;
    left: 0;
    width: 1200px;
    text-align: center;
  }
  .intro__lead {
    margin: 0;
    font-weight: 700;
    font-size: 31px;
    line-height: 1.2;
  }
  .intro__lead strong {
    display: block;
    font-size: 40px;
    line-height: 1.25;
  }
  .intro__note {
    margin: 24px 0 0;
    font-style: italic;
    font-weight: 500;
    font-size: 28px;
    line-height: 1.45;
  }
  .brand {
    position: absolute;
    left: 88px;
    top: 322px;
    width: 170px;
    color: var(--navy-text);
  }
  .brand__mark {
    width: 70px;
    height: 70px;
    background: var(--navy);
  }
  .brand__name {
    margin: 10px 0 0;
    font-weight: 700;
    font-size: 20px;
    line-height: 1.1;
  }
  .contact {
    position: absolute;
    left: 276px;
    top: 316px;
    color: var(--navy-text);
    font-weight: 700;
  }
  .contact__web {
    margin: 0;
    font-size: 41px;
    letter-spacing: 0.5px;
    line-height: 1.1;
  }
  .contact__email {
    margin: 4px 0 0;
    font-weight: 600;
    font-size: 27px;
    letter-spacing: 0.4px;
  }
  .phone {
    position: absolute;
    right: 68px;
    top: 466px;
    margin: 0;
    color: var(--navy-text);
    font-weight: 600;
    font-size: 44px;
  }
  .social {
    position: absolute;
    left: 858px;
    top: 540px;
    display: flex;
    gap: 7px;
  }
  .social span {
    width: 36px;
    height: 36px;
    border-radius: 5px;
    background: linear-gradient(#6fb6e6, #2f78b6);
  }
  .invite {
    position: absolute;
    left: 690px;
    top: 684px;
    width: 466px;
    margin: 0;
    text-align: center;
    font-style: italic;
    font-weight: 600;
    font-size: 26px;
    line-height: 1.42;
  }
</style>
</head>
<body>
<main class="postcard">
  <svg class="postcard__shapes" width="1200" height="926" viewBox="0 0 1200 926" aria-hidden="true">
    <defs>
      <linearGradient id="bgNavy" x1="0" y1="0" x2="0" y2="1">
        <stop offset="0" stop-color="#1f3a50"/>
        <stop offset="0.3" stop-color="#132636"/>
        <stop offset="1" stop-color="#0d1b27"/>
      </linearGradient>
      <linearGradient id="bandOrange" x1="0" y1="0" x2="0" y2="1">
        <stop offset="0" stop-color="#f5921e"/>
        <stop offset="1" stop-color="#f08a16"/>
      </linearGradient>
      <linearGradient id="waveNavy" x1="0" y1="0" x2="1" y2="0">
        <stop offset="0" stop-color="#2a4b66"/>
        <stop offset="0.5" stop-color="#1b344a"/>
        <stop offset="1" stop-color="#2a4b66"/>
      </linearGradient>
    </defs>
    <rect width="1200" height="926" fill="url(#bgNavy)"/>
    <rect x="0" y="284" width="1200" height="3" fill="#3b5a74"/>
    <path d="M0,287 H1200 V520 C1060,600 900,640 760,590 C600,530 470,440 300,470 C180,492 80,560 0,600 Z" fill="url(#bandOrange)"/>
    <path d="M0,600 C80,560 180,492 300,470 C470,440 600,530 760,590 C900,640 1060,600 1200,520 V560 C1060,650 900,680 740,625 C590,570 470,500 310,520 C190,535 90,600 0,650 Z" fill="url(#waveNavy)"/>
    <path d="M20,640 C110,585 200,535 310,522 C460,505 580,560 700,612" fill="none" stroke="#6f93ae" stroke-width="4"/>
  </svg>

  <svg class="postcard__shapes" width="1200" height="926" viewBox="0 0 1200 926">
    <defs>
      <linearGradient id="kitchenTone" x1="0" y1="0" x2="0" y2="1">
        <stop offset="0" stop-color="#a87448"/>
        <stop offset="0.45" stop-color="#7b4622"/>
        <stop offset="0.75" stop-color="#3a2a22"/>
        <stop offset="1" stop-color="#c3ae8e"/>
      </linearGradient>
    </defs>
    <path role="img" aria-label="Photo of a finished kitchen remodel with wood cabinets and a dark granite island"
          d="M31,672 C120,615 210,560 315,548 C460,532 580,585 687,630 V895 H31 Z"
          fill="url(#kitchenTone)"/>
  </svg>

  <section class="intro">
    <p class="intro__lead">We are currently working with one of your neighbors
      <strong>and would love the opportunity to work for you.</strong></p>
    <p class="intro__note">You can look us up on our website and see<br>some of the wonderful spaces we have helped create.</p>
  </section>

  <div class="brand">
    <div class="brand__mark"></div>
    <p class="brand__name">BELTRANE<br>HOME WORKS</p>
  </div>

  <div class="contact">
    <p class="contact__web">WWW.BELTRANEHOMEWORKS.EXAMPLE</p>
    <p class="contact__email">BELTRANEHOMEWORKS@MAILBOX.EXAMPLE</p>
  </div>

  <p class="phone">Tel: 913-552-0187</p>

  <div class="social" aria-hidden="true"><span></span><span></span><span></span></div>

  <p class="invite">Call us today to<br>schedule an appointment<br>and let us know how we can<br>help you create the new space<br>you have always dreamed of!</p>
</main>
</body>
</html>
```